Poster - Series of Poster Designs

We have a number of motivational quotes related to weight loss and fitness which need putting into a series of posters.
The designs need to:
- Reflect the current brand (see www.bluefernhaven.com.au)
- Be designed with scalability in mind to fit to A1, A3, A4, and A5. All portrait layout.
- Incorporate our logo
- Any images need to relfect the diversity of our clients ranging from 70kgs up to 200kgs.
- We have a stock of photos which can be used, or you can source your own (subject to budget approval)
Total of 26 posters in total, but all on the same design series (so effectively 1 design, with 26 applications).
The series of quotes are attached. An example quote would be:
-
"The difference between your body this week and next week is what you do for the next seven days to achieve your goals"
-
Our clients are a range of ages (20 - 60) and split male/female so colours should be neutral and reflect our orange/green branding. A modern feel but not super modern.
Output needs to be A3 ready to print with all source files included so that we can amend in the future.
There may be ongoing work for the right designer.

```html
<!DOCTYPE html>
<html lang="en">
<head>
<meta charset="utf-8">
<title>Bluefern Haven – Motivational Poster</title>
<link href="https://fonts.googleapis.com/css2?family=Cabin:wght@600&family=Cormorant+Garamond:ital,wght@1,500&display=swap" rel="stylesheet">
<style>
  :root {
    --orange: #f7941d;
    --green: #8dc63f;
    --coral: #f5855a;
    --ink: #333333;
    --grey: #6d6e71;
    --curl: #2f3b3b;
    --paper: #ffffff;
  }
  html, body {
    margin: 0;
    padding: 0;
    overflow: hidden;
    background: var(--paper);
  }
  .poster {
    position: relative;
    width: 846px;
    height: 1200px;
    overflow: hidden;
    background: var(--paper);
  }
  .brand {
    position: absolute;
    top: 62px;
    left: 0;
    width: 846px;
    text-align: center;
    font-family: "Cabin", sans-serif;
    font-weight: 600;
  }
  .brand-name {
    display: block;
    font-size: 50px;
    line-height: 56px;
    color: var(--ink);
  }
  .brand-tagline {
    display: block;
    font-size: 15px;
    letter-spacing: 1px;
    color: var(--grey);
    margin-top: 2px;
  }
  .banner {
    position: absolute;
    top: 0;
    left: 0;
  }
  .quote {
    position: absolute;
    top: 562px;
    left: 30px;
    width: 786px;
    margin: 0;
    text-align: center;
    font-family: "Cormorant Garamond", serif;
    font-style: italic;
    font-weight: 500;
    font-size: 68px;
    line-height: 80px;
    color: var(--orange);
  }
  .quote .accent { color: var(--green); }
  .cta {
    position: absolute;
    top: 1040px;
    left: 0;
    width: 846px;
    text-align: center;
    font-family: "Cabin", sans-serif;
    font-weight: 600;
    font-size: 30px;
    line-height: 34px;
  }
  .cta-phone { color: var(--ink); }
  .cta-brochure { color: var(--green); }
  .cta-request { color: var(--coral); }
</style>
</head>
<body>
<main class="poster">
  <header class="brand">
    <span class="brand-name">Bluefern Haven</span>
    <span class="brand-tagline">WEIGHT LOSS RETREAT</span>
  </header>

  <svg class="banner" width="846" height="1200" viewBox="0 0 846 1200" xmlns="http://www.w3.org/2000/svg">
    <defs>
      <linearGradient id="beach-tones" x1="0" y1="0" x2="0" y2="1">
        <stop offset="0" stop-color="#c7a267"/>
        <stop offset="0.22" stop-color="#d9c5a0"/>
        <stop offset="0.42" stop-color="#e8dcc6"/>
        <stop offset="0.7" stop-color="#f4eee5"/>
        <stop offset="1" stop-color="#fdfbf9"/>
      </linearGradient>
      <linearGradient id="sea-tones" x1="1" y1="0" x2="0.4" y2="0.6">
        <stop offset="0" stop-color="#8fb3d0" stop-opacity="0.9"/>
        <stop offset="0.45" stop-color="#a9c6d8" stop-opacity="0.45"/>
        <stop offset="1" stop-color="#e8dcc6" stop-opacity="0"/>
      </linearGradient>
      <clipPath id="banner-shape">
        <path d="M30 178 Q423 222 816 178 L816 1022 Q423 990 30 1022 Z"/>
      </clipPath>
    </defs>

    <g clip-path="url(#banner-shape)" role="img" aria-label="Photo of a group of walkers with backpacks strolling along a sandy beach beneath sunlit cliffs beside the sea">
      <rect x="30" y="170" width="786" height="860" fill="url(#beach-tones)"/>
      <rect x="30" y="170" width="786" height="860" fill="url(#sea-tones)"/>
    </g>

    <g class="banner-curls" fill="var(--curl)">
      <path d="M30 178 L30 230 Q10 224 3 204 Q10 184 30 178 Z"/>
      <path d="M816 178 L816 230 Q836 224 843 204 Q836 184 816 178 Z"/>
      <path d="M30 1022 L30 972 Q10 978 3 998 Q10 1018 30 1022 Z"/>
      <path d="M816 1022 L816 972 Q836 978 843 998 Q836 1018 816 1022 Z"/>
    </g>
  </svg>

  <p class="quote">
    <span class="accent">Stop</span> beating yourself&nbsp; up!<br>
    You are a <span class="accent">work</span> in progress,<br>
    which means you<br>
    get there a little at a <span class="accent">time</span>.<br>
    Not all at once.
  </p>

  <footer class="cta">
    <div class="cta-phone">Call 1300 555 218</div>
    <div class="cta-brochure">Free Brochure</div>
    <div class="cta-request">Request Now!</div>
  </footer>
</main>
</body>
</html>
```